Banner required for our website Sale of Silent Domestic Rangehoods

These images around silence are very good however, even more important are the family conversations that happen within the kitchen area.
These conversations are often disrupted by the use of a noisy rangehood.
A Family photos in the kitchen with a tag line relating to regaining those precious moments would be a great concept.
Regards Neil
Just a few suggestions.
I would prefer no illistrations.
Most importantly I am still seeking a visual to highlite the silent benifit of our rangehoods.The best visual will most like win this contest. We currently use the lady with the finger held to her mouth. Any other suggestions would be greatly appreciated.
We need a banner ad for the sale of designer silent domestic rangehoods.
These rangehood are aimed at the middle to higher income buyers, they are Elegant, efficient and powerful.
We aim to offer a product that exceeds our customers expectations.
Visit our website and everything we do is self explainatory.
www.mirovale.com.au
Regards Neil
Updates
Mirovale Silent rangehoods enable the family to again enjoy conversations in the kitchen
You can have friends over, revel in each others company and enjoy a great lunch or dinner without the distraction of a rangehood that sounds like a jet engine.
They also simply work better
Our promo banners typically have 2 sizes: 500x500 pixels for our socials, and a 2570*730 pixels for our Promotions page
Target Market(s)
Renovators, second home buyers, ladies between 28 and 49 years of age
Requirements
Must have
- Appealing visuals, upmarket look and feel.
Nice to have
- Family picture with kids.
Should not have
- The words Cheap, Budget nor afforadable.

```html
<!DOCTYPE html>
<html lang="en">
<head>
<meta charset="utf-8">
<title>Mirovale Silent Rangehoods – Promo Banners</title>
<link rel="stylesheet" href="https://fonts.googleapis.com/css2?family=Poppins:wght@400;500;800&display=swap">
<style>
  :root {
    --stage: #88ecfe;
    --pink: #de0a6b;
    --ink: #0d0d0d;
    --paper: #fdf4f8;
    --paper-edge: #ffffff;
    --night: #1b1719;
    --night-plum: #2b1321;
    --white: #ffffff;
    --photo-top: #e9e7e4;
    --photo-mid: #cfcac3;
    --photo-low: #6e5a47;
  }
  * { box-sizing: border-box; margin: 0; padding: 0; }
  html, body { width: 1200px; height: 960px; overflow: hidden; }
  body {
    background: var(--stage);
    font-family: "Poppins", sans-serif;
    position: relative;
  }
  .banner {
    position: absolute;
    left: 58px;
    width: 1083px;
    height: 308px;
    overflow: hidden;
  }
  .banner--light {
    top: 145px;
    background: linear-gradient(90deg, var(--paper-edge) 0%, var(--paper) 45%, var(--paper) 100%);
    color: var(--ink);
  }
  .banner--dark {
    top: 508px;
    background: linear-gradient(110deg, var(--night) 0%, var(--night) 40%, var(--night-plum) 75%, var(--night) 100%);
    color: var(--white);
  }
  .banner__art {
    position: absolute;
    inset: 0;
    width: 1083px;
    height: 308px;
  }
  .headline {
    position: absolute;
    left: 21px;
    top: 17px;
    font-weight: 800;
    font-size: 44px;
    line-height: 50px;
    letter-spacing: -1.5px;
    text-transform: uppercase;
    white-space: nowrap;
  }
  .headline__accent { color: var(--pink); }
  .intro {
    position: absolute;
    left: 22px;
    top: 122px;
    width: 430px;
    font-size: 11px;
    line-height: 12.8px;
    font-weight: 400;
    white-space: nowrap;
  }
  .features {
    position: absolute;
    left: 22px;
    top: 185px;
    width: 540px;
    list-style: none;
    display: grid;
    grid-template-columns: 279px 260px;
    row-gap: 11px;
  }
  .feature {
    display: flex;
    align-items: center;
    gap: 6px;
    font-size: 12.6px;
    font-weight: 400;
    height: 22px;
    white-space: nowrap;
  }
  .feature__tick { width: 23px; height: 23px; flex: none; }
  .feature__em { color: var(--pink); }
  .cta {
    position: absolute;
    left: 0;
    top: 256px;
    width: 306px;
    height: 44px;
    background: var(--pink);
    border-radius: 0 18px 18px 0;
    color: var(--white);
    font-weight: 800;
    font-size: 23px;
    letter-spacing: -0.3px;
    line-height: 44px;
    padding-left: 22px;
    text-transform: uppercase;
    white-space: nowrap;
  }
</style>
</head>
<body>

  <section class="banner banner--light" aria-label="Mirovale silent rangehood promotion, light version">
    <svg class="banner__art" viewBox="105 260 1945 553" preserveAspectRatio="none">
      <g class="stripes" fill="#fbe3ee" opacity="0.7">
        <polygon points="1150,260 1500,260 1100,813 750,813"/>
        <polygon points="1560,260 1700,260 1300,813 1160,813"/>
        <polygon points="1950,390 2030,410 1760,813 1660,813"/>
      </g>
      <circle cx="968" cy="352" r="8" fill="none" stroke="#f2a9c8" stroke-width="3"/>
      <path d="M1083,526 l14,14 M1097,526 l-14,14" stroke="#f2a9c8" stroke-width="3"/>
      <path d="M1922,619 l13,13 M1935,619 l-13,13" stroke="#f2a9c8" stroke-width="3"/>
      <path d="M1038,728 l12,-8 l8,14" fill="none" stroke="#f2a9c8" stroke-width="3"/>
      <path class="photo-frame" fill="var(--pink)" d="M1290,310 L1740,284 Q1775,282 1790,300 L1840,350 Q1857,365 1857,390 L1857,700 Q1857,735 1830,750 L1790,785 Q1770,798 1740,796 L1290,768 Q1250,765 1225,745 L1160,700 Q1135,690 1135,660 L1135,430 Q1135,395 1160,385 L1225,330 Q1250,312 1290,310 Z"/>
      <defs>
        <linearGradient id="kitchenTones" x1="0" y1="0" x2="0" y2="1">
          <stop offset="0" stop-color="var(--photo-top)"/>
          <stop offset="0.55" stop-color="var(--photo-mid)"/>
          <stop offset="1" stop-color="var(--photo-low)"/>
        </linearGradient>
      </defs>
      <path class="photo" role="img" aria-label="Photo of a bright modern kitchen with a stainless rangehood, white island bench and bar stools" fill="url(#kitchenTones)" d="M1230,338 L1790,310 Q1830,308 1830,350 L1830,735 Q1830,775 1790,773 L1230,745 Q1162,742 1162,690 L1162,395 Q1162,342 1230,338 Z"/>
    </svg>

    <h1 class="headline">Silent. <span class="headline__accent">Powerful.</span><br>Beautiful.</h1>
    <p class="intro">Mirovale Silent rangehoods enable the family to again enjoy conversations<br>in the kitchen You can have friends over, revel in each others company and<br>enjoy a great lunch or dinner without the distraction of a rangehood that<br>sounds like a jet engine</p>
    <ul class="features">
      <li class="feature"><svg class="feature__tick" viewBox="0 0 24 24"><path d="M19 8.5 A9.5 9.5 0 1 1 15.5 4" fill="none" stroke="var(--pink)" stroke-width="2"/><path d="M7 11.5 l4 4.5 L21 2.5" fill="none" stroke="var(--pink)" stroke-width="2.2" stroke-linecap="round" stroke-linejoin="round"/></svg><span><span class="feature__em">German engineered</span> Australian owned</span></li>
      <li class="feature"><svg class="feature__tick" viewBox="0 0 24 24"><path d="M19 8.5 A9.5 9.5 0 1 1 15.5 4" fill="none" stroke="var(--pink)" stroke-width="2"/><path d="M7 11.5 l4 4.5 L21 2.5" fill="none" stroke="var(--pink)" stroke-width="2.2" stroke-linecap="round" stroke-linejoin="round"/></svg><span><span class="feature__em">10-year</span> motor warranty</span></li>
      <li class="feature"><svg class="feature__tick" viewBox="0 0 24 24"><path d="M19 8.5 A9.5 9.5 0 1 1 15.5 4" fill="none" stroke="var(--pink)" stroke-width="2"/><path d="M7 11.5 l4 4.5 L21 2.5" fill="none" stroke="var(--pink)" stroke-width="2.2" stroke-linecap="round" stroke-linejoin="round"/></svg><span><span class="feature__em">3x more</span> energy-efficient</span></li>
      <li class="feature"><svg class="feature__tick" viewBox="0 0 24 24"><path d="M19 8.5 A9.5 9.5 0 1 1 15.5 4" fill="none" stroke="var(--pink)" stroke-width="2"/><path d="M7 11.5 l4 4.5 L21 2.5" fill="none" stroke="var(--pink)" stroke-width="2.2" stroke-linecap="round" stroke-linejoin="round"/></svg><span><span class="feature__em">Free ducting</span> included</span></li>
    </ul>
    <div class="cta">Simply work better</div>
  </section>

  <section class="banner banner--dark" aria-label="Mirovale silent rangehood promotion, dark version">
    <svg class="banner__art" viewBox="105 260 1945 553" preserveAspectRatio="none">
      <g class="stripes" fill="#3a1828" opacity="0.45">
        <polygon points="1150,260 1500,260 1100,813 750,813"/>
        <polygon points="1560,260 1700,260 1300,813 1160,813"/>
      </g>
      <circle cx="968" cy="352" r="8" fill="none" stroke="#5b2a40" stroke-width="3"/>
      <path d="M1083,526 l14,14 M1097,526 l-14,14" stroke="#6b2240" stroke-width="3"/>
      <path d="M1922,619 l13,13 M1935,619 l-13,13" stroke="#8a1a4a" stroke-width="3"/>
      <path d="M1038,728 l12,-8 l8,14" fill="none" stroke="#5b2a40" stroke-width="3"/>
      <path class="photo-frame" fill="var(--pink)" d="M1290,310 L1740,284 Q1775,282 1790,300 L1840,350 Q1857,365 1857,390 L1857,700 Q1857,735 1830,750 L1790,785 Q1770,798 1740,796 L1290,768 Q1250,765 1225,745 L1160,700 Q1135,690 1135,660 L1135,430 Q1135,395 1160,385 L1225,330 Q1250,312 1290,310 Z"/>
      <defs>
        <linearGradient id="kitchenTonesDark" x1="0" y1="0" x2="0" y2="1">
          <stop offset="0" stop-color="var(--photo-top)"/>
          <stop offset="0.55" stop-color="var(--photo-mid)"/>
          <stop offset="1" stop-color="var(--photo-low)"/>
        </linearGradient>
      </defs>
      <path class="photo" role="img" aria-label="Photo of a bright modern kitchen with a stainless rangehood, white island bench and bar stools" fill="url(#kitchenTonesDark)" d="M1230,338 L1790,310 Q1830,308 1830,350 L1830,735 Q1830,775 1790,773 L1230,745 Q1162,742 1162,690 L1162,395 Q1162,342 1230,338 Z"/>
    </svg>

    <h1 class="headline">Silent. <span class="headline__accent">Powerful.</span><br>Beautiful.</h1>
    <p class="intro">Mirovale Silent rangehoods enable the family to again enjoy conversations<br>in the kitchen You can have friends over, revel in each others company and<br>enjoy a great lunch or dinner without the distraction of a rangehood that<br>sounds like a jet engine</p>
    <ul class="features">
      <li class="feature"><svg class="feature__tick" viewBox="0 0 24 24"><path d="M19 8.5 A9.5 9.5 0 1 1 15.5 4" fill="none" stroke="var(--pink)" stroke-width="2"/><path d="M7 11.5 l4 4.5 L21 2.5" fill="none" stroke="var(--pink)" stroke-width="2.2" stroke-linecap="round" stroke-linejoin="round"/></svg><span>German engineered Australian owned</span></li>
      <li class="feature"><svg class="feature__tick" viewBox="0 0 24 24"><path d="M19 8.5 A9.5 9.5 0 1 1 15.5 4" fill="none" stroke="var(--pink)" stroke-width="2"/><path d="M7 11.5 l4 4.5 L21 2.5" fill="none" stroke="var(--pink)" stroke-width="2.2" stroke-linecap="round" stroke-linejoin="round"/></svg><span>10-year motor warranty</span></li>
      <li class="feature"><svg class="feature__tick" viewBox="0 0 24 24"><path d="M19 8.5 A9.5 9.5 0 1 1 15.5 4" fill="none" stroke="var(--pink)" stroke-width="2"/><path d="M7 11.5 l4 4.5 L21 2.5" fill="none" stroke="var(--pink)" stroke-width="2.2" stroke-linecap="round" stroke-linejoin="round"/></svg><span>3x more energy-efficient</span></li>
      <li class="feature"><svg class="feature__tick" viewBox="0 0 24 24"><path d="M19 8.5 A9.5 9.5 0 1 1 15.5 4" fill="none" stroke="var(--pink)" stroke-width="2"/><path d="M7 11.5 l4 4.5 L21 2.5" fill="none" stroke="var(--pink)" stroke-width="2.2" stroke-linecap="round" stroke-linejoin="round"/></svg><span>Free ducting included</span></li>
    </ul>
    <div class="cta">Simply work better</div>
  </section>

</body>
</html>
```